I need a business card representing my company, VELDRA, it's an artist management and design company. Complete name is "VELDRA Artist Mgmt. + Design Co." I need it to be world class and very appealing, sophisticated and artistically unique.
Updates

Posted an updated Brief please see. I need a business card representing my company, VELDRA, it's an artist management and design company. Complete name is "VELDRA Artist Mgmt. + Design Co." I need it to be world class and very appealing, sophisticated and artistically unique.

Designs look the same

Designs look the same

Target Market(s)

Advertisers, Entertainment Companies, Commercial companies

Industry/Entity Type

Advertising

Contact Information for Business Card

I need a business card representing my company, VELDRA, it's an artist management and design company. Complete name is "VELDRA Artist Mgmt. + Design Co." I need it to be world class and very appealing, sophisticated and artistically unique. One side can be VELDRA Artist Mgmt. + Design Co. and the other my name, Teodoro Lindqvist, my contact telephone: 412.638.2957, email veldraartist@plumora.net, my address: 3264 Harwell Ave. #517 Miami, FL 33184

Font styles to use
Other font styles liked:
• Calibri

Colors
ffffff
0455a3
f37122

Requirements
Must have
• "VELDRA" stand out bigger than the rest of the text.
Nice to have
• Name "VELDRA" can be centered on one side or in the corner or along side edges, just need something cool and different.
Should not have
• I am open just try to keep it clean looking

```html
<!DOCTYPE html>
<html lang="en">
<head>
<meta charset="utf-8">
<title>VELDRA Artist Mgmt. + Design Co. — Business Card</title>
<link rel="stylesheet" href="https://fonts.googleapis.com/css2?family=Kanit:wght@200;300;400;500;600&display=swap">
<style>
  :root {
    --backdrop: #c0c0c2;
    --card-dark: #2a2627;
    --card-light: #ffffff;
    --ink: #1e1e1e;
    --white: #ffffff;
    --accent-orange: #f37122;
    --accent-blue: #0455a3;
    --font-main: "Kanit", sans-serif;
  }
  * { box-sizing: border-box; margin: 0; padding: 0; }
  html, body {
    width: 1200px;
    height: 1000px;
    overflow: hidden;
    background: var(--backdrop);
    font-family: var(--font-main);
  }
  .canvas {
    position: relative;
    width: 1200px;
    height: 1000px;
  }
  .card {
    position: absolute;
    left: 280px;
    width: 640px;
    height: 366px;
    border-radius: 26px;
    overflow: hidden;
    box-shadow: 0 6px 18px rgba(0,0,0,0.18);
  }
  /* Front side */
  .card--front {
    top: 100px;
    background: var(--card-dark);
  }
  .accent-bar {
    position: absolute;
    width: 16px;
  }
  .accent-bar--orange {
    left: 0;
    top: 44px;
    height: 116px;
    background: var(--accent-orange);
  }
  .accent-bar--blue {
    right: 0;
    top: 210px;
    height: 116px;
    background: var(--accent-blue);
  }
  .brand {
    position: absolute;
    left: 0;
    right: 0;
    top: 104px;
    display: flex;
    flex-direction: column;
    align-items: center;
    color: var(--white);
  }
  .brand__name {
    font-family: var(--font-main);
    font-weight: 500;
    font-size: 110px;
    line-height: 1;
    letter-spacing: 2px;
  }
  .brand__tagline {
    align-self: flex-start;
    margin-top: 4px;
    margin-left: 172px;
    font-weight: 200;
    font-size: 21px;
    letter-spacing: 0.5px;
  }
  /* Back side */
  .card--back {
    top: 534px;
    background: var(--card-light);
    color: var(--ink);
  }
  .info-row {
    position: absolute;
    display: flex;
    align-items: center;
    gap: 16px;
    font-size: 16px;
    font-weight: 300;
    letter-spacing: 0.6px;
    white-space: nowrap;
  }
  .info-row--top { left: 0; right: 28px; top: 26px; }
  .info-row--bottom { left: 26px; right: 0; top: 314px; }
  .rule {
    flex: 1;
    height: 2px;
    background: var(--ink);
  }
  .holder-name {
    position: absolute;
    left: 0;
    right: 0;
    top: 148px;
    text-align: center;
    font-size: 44px;
    font-weight: 500;
    letter-spacing: 1px;
  }
</style>
</head>
<body>
<main class="canvas">
  <section class="card card--front" aria-label="Business card front">
    <span class="accent-bar accent-bar--orange"></span>
    <span class="accent-bar accent-bar--blue"></span>
    <div class="brand">
      <span class="brand__name">VELDRA</span>
      <span class="brand__tagline">Artist Mgmt. + Design Co</span>
    </div>
  </section>

  <section class="card card--back" aria-label="Business card back">
    <div class="info-row info-row--top">
      <span class="rule"></span>
      <p class="address">3264 Harwell Ave. #517 Miami, FL 33184</p>
    </div>
    <h1 class="holder-name">Teodoro Lindqvist</h1>
    <div class="info-row info-row--bottom">
      <p class="contact">412.638.2957 | veldraartist@plumora.net</p>
      <span class="rule"></span>
    </div>
  </section>
</main>
</body>
</html>
```